Full page ad in a magazine

We would like an ad designed to be placed for advertising in magazines, theater playbills, etc. I have attached a copy of some previous ads that were done for us, although they need much improvement and redesigned. We have won "best chiropractor" awards that can be seen on our website home page at harlowspineandjoint.example

```html
<!DOCTYPE html>
<html lang="en">
<head>
<meta charset="utf-8">
<title>Harlow Spine &amp; Joint Center – Magazine Ad</title>
<link href="https://fonts.googleapis.com/css2?family=Bebas+Neue&family=Lato:wght@400;700;900&display=swap" rel="stylesheet">
<style>
  :root{
    --maroon:#860203;
    --gold:#f7b90f;
    --ink:#231f20;
    --grey:#8c8c8c;
    --paper:#ffffff;
    --badge-blue:#2f4ea0;
    --badge-dark:#1a1a1a;
  }
  *{box-sizing:border-box;margin:0;padding:0}
  html,body{width:1200px;height:1200px;overflow:hidden;background:var(--paper)}
  body{position:relative;font-family:'Lato',sans-serif;color:var(--ink)}
  .ad{position:absolute;left:251px;top:107px;width:697px;height:986px;background:var(--paper);
      box-shadow:0 2px 14px rgba(0,0,0,.12);overflow:hidden}
  .abs{position:absolute}

  /* brand */
  .brand{left:29px;top:28px;height:104px;display:flex;align-items:center;gap:14px;z-index:2}
  .brand-mark{width:95px;height:104px;background:var(--maroon);flex:none}
  .brand-name{font-family:'Lato',sans-serif;font-weight:900;color:var(--maroon);font-size:28px;line-height:1.12;letter-spacing:1px;width:330px}

  /* hero band */
  .hero-band{left:0;top:163px;width:470px;height:107px;background:var(--maroon)}
  .hero-title{left:28px;top:170px;font-family:'Bebas Neue',sans-serif;font-size:64px;line-height:1;color:#fff;letter-spacing:.3px}
  .hero-sub{left:28px;top:229px;font-size:21px;color:#fff;letter-spacing:.3px}

  .hero-visual{left:0;top:0;width:697px;height:986px}

  /* treating list */
  .treating-label{left:28px;top:288px;font-weight:700;font-size:20px}
  .conditions{left:28px;top:322px;display:grid;grid-template-columns:189px 160px;row-gap:17px;list-style:none}
  .condition{display:flex;align-items:center;gap:13px;font-size:19px;height:38px}
  .condition-icon{width:28px;height:36px;border-radius:50%;background:radial-gradient(circle at 40% 45%,#b4343a 0 35%,var(--gold) 36%);flex:none}

  .insurance{left:0;top:492px;width:390px;height:22px;background:linear-gradient(90deg,var(--gold) 0 40%,rgba(247,185,15,0))}
  .insurance-text{left:28px;top:494px;font-weight:700;font-size:14px}

  /* contact */
  .doctor{left:29px;top:543px;width:103px;height:129px}
  .doctor-photo{width:103px;height:113px;background:linear-gradient(160deg,#6e7278,#3b3d42)}
  .doctor-name{height:16px;background:var(--maroon);color:#fff;font-weight:700;font-size:10.5px;line-height:16px;text-align:center}
  .phone{left:140px;top:537px;font-family:'Bebas Neue',sans-serif;font-size:56px;line-height:1;letter-spacing:.5px}
  .hours{left:140px;top:590px;width:233px;height:17px;background:var(--maroon);color:#fff;font-weight:700;font-size:14px;line-height:17px;text-align:center}
  .pin{left:143px;top:624px}
  .location{left:194px;top:620px;font-size:15px;line-height:18.5px}
  .location strong{font-weight:700}

  /* awards */
  .awards-tab{left:28px;top:704px;width:173px;height:22px;background:var(--gold);border-radius:4px 12px 0 0;
      font-weight:700;font-size:9.5px;line-height:22px;padding-left:20px}
  .awards-frame{left:28px;top:723px;width:446px;height:142px;border:2px solid var(--gold);border-radius:0 0 10px 0;border-left:none}
  .award-seal{left:45px;top:752px;width:86px;height:86px;border-radius:50%;background:var(--badge-dark);box-shadow:0 0 0 4px var(--gold)}
  .award-card{top:738px;height:113px;background:var(--badge-blue)}
  .award-card.a{left:182px;width:110px}
  .award-card.b{left:326px;width:135px}

  /* vote */
  .vote-band{left:120px;top:897px;width:430px;height:30px;background:linear-gradient(90deg,rgba(247,185,15,0),rgba(247,185,15,.85))}
  .vote-icon{left:28px;top:899px}
  .vote-label{left:63px;top:899px;font-weight:700;font-size:14px;line-height:14px}
  .vote-divider{left:125px;top:899px;width:1.5px;height:28px;background:var(--maroon)}
  .vote-url{left:135px;top:903px;font-size:15px}

  .footer{left:0;top:938px;width:697px;height:48px;background:var(--maroon)}
  .footer-url{left:28px;top:947px;color:#fff;font-size:22px;letter-spacing:.3px}
</style>
</head>
<body>
<main class="ad">

  <div class="abs hero-band"></div>

  <svg class="abs hero-visual" viewBox="0 0 697 986" role="img" aria-label="Photo of a man holding his neck with a glowing spine, flowing into an illustrated spinal column">
    <defs>
      <linearGradient id="visualTone" x1="0" y1="0" x2="0" y2="1">
        <stop offset="0" stop-color="#2e2a29"/>
        <stop offset=".35" stop-color="#5c4d47"/>
        <stop offset=".6" stop-color="#d9d6d3"/>
        <stop offset="1" stop-color="#bfbcba"/>
      </linearGradient>
      <radialGradient id="spineGlow" cx=".6" cy=".45" r=".45">
        <stop offset="0" stop-color="#ff7a1a" stop-opacity=".85"/>
        <stop offset="1" stop-color="#ff7a1a" stop-opacity="0"/>
      </radialGradient>
    </defs>
    <path d="M540 60 L697 60 L697 986 L525 986 L485 880 L432 700 L372 530 L380 400 L440 330 L455 270 L490 200 Z" fill="url(#visualTone)"/>
    <path d="M540 60 L697 60 L697 986 L525 986 L485 880 L432 700 L372 530 L380 400 L440 330 L455 270 L490 200 Z" fill="url(#spineGlow)"/>
  </svg>

  <div class="abs brand">
    <div class="brand-mark"></div>
    <div class="brand-name">HARLOW<br>SPINE &amp; JOINT<br>CENTER</div>
  </div>

  <h1 class="abs hero-title">NECK OR BACK PAIN?</h1>
  <p class="abs hero-sub">CHIROPRACTIC &nbsp;•&nbsp; MASSAGE</p>

  <h2 class="abs treating-label">Treating:</h2>
  <ul class="abs conditions">
    <li class="condition"><span class="condition-icon" role="img" aria-label="Back pain pictogram"></span>BACK PAIN</li>
    <li class="condition"><span class="condition-icon" role="img" aria-label="Joint pain pictogram"></span>JOINT PAIN</li>
    <li class="condition"><span class="condition-icon" role="img" aria-label="Neck pain pictogram"></span>NECK PAIN</li>
    <li class="condition"><span class="condition-icon" role="img" aria-label="Sciatica pictogram"></span>SCIATICA</li>
    <li class="condition"><span class="condition-icon" role="img" aria-label="Headache pictogram"></span>HEADACHES</li>
    <li class="condition"><span class="condition-icon" role="img" aria-label="Fatigue pictogram"></span>FATIGUE</li>
  </ul>

  <div class="abs insurance"></div>
  <p class="abs insurance-text">Medicare and most Insurance accepted</p>

  <figure class="abs doctor">
    <div class="doctor-photo" role="img" aria-label="Portrait of the chiropractor in a suit"></div>
    <figcaption class="doctor-name">Dr. Evan Marsh DC</figcaption>
  </figure>
  <p class="abs phone">555.014.2290</p>
  <p class="abs hours">OPEN MONDAY - SATURDAY</p>

  <svg class="abs pin" width="44" height="44" viewBox="0 0 44 44" fill="none" stroke="#231f20" stroke-width="1.4">
    <path d="M22 4a11 11 0 0 1 11 11c0 8-11 19-11 19S11 23 11 15A11 11 0 0 1 22 4z"/>
    <circle cx="22" cy="15" r="5.5"/>
    <path d="M13 28 L4 40 L16 36 L28 40 L40 36 L33 28"/>
  </svg>
  <p class="abs location"><strong>MIDTOWN LOCATION</strong><br>1270 Larkspur Ave., #204<br>Harlow, VA 23999</p>

  <div class="abs awards-frame"></div>
  <div class="abs awards-tab">BEST CHIROPRACTOR AWARDS</div>
  <div class="abs award-seal" role="img" aria-label="Readers' choice award badge"></div>
  <div class="abs award-card a" role="img" aria-label="Best of gold winner badge 2022"></div>
  <div class="abs award-card b" role="img" aria-label="Best of gold winner badge 2021"></div>

  <div class="abs vote-band"></div>
  <svg class="abs vote-icon" width="30" height="28" viewBox="0 0 30 28" fill="none" stroke="#860203" stroke-width="1.5">
    <circle cx="13" cy="15" r="11"/>
    <path d="M9 18 L16 8 L22 12 L17 22 Z"/>
  </svg>
  <p class="abs vote-label">VOTE<br>FOR US</p>
  <div class="abs vote-divider"></div>
  <p class="abs vote-url">www.tidewaterpicks.example/bestof</p>

  <div class="abs footer"></div>
  <p class="abs footer-url">www.harlowspineandjoint.example</p>

</main>
</body>
</html>
```